Designing a label for Convertible Hood Cleaner (also 6 more labels to design in the future)

We have a range of cleaning products which we need to update label designs

This competition is just for one design but once a winner has been selected we have a lot more work for you including 6 more labels and a new logo.

Please see files for content. This product is very popular but the label is outdated.

Size of label - 110mm x 75mm
This will be a sticky label to be added to a sachet (white ziplock pouch)

Colors

Designer to choose colors to be used in the design.

```html
<!DOCTYPE html>
<html lang="en">
<head>
<meta charset="utf-8">
<title>Heavy Duty Convertible Soft Top Cleaner – Label</title>
<link href="https://fonts.googleapis.com/css2?family=Archivo+Black&display=swap" rel="stylesheet">
<style>
  :root {
    --label-blue: #4a89c9;
    --label-red: #e8232a;
    --label-white: #ffffff;
    --ink-black: #111111;
    --tag-blue: #3f7fc1;
    --photo-light: #e4e6e8;
    --photo-dark: #2a2c30;
  }
  html, body {
    margin: 0;
    padding: 0;
    width: 892px;
    height: 1200px;
    overflow: hidden;
    background: var(--label-blue);
  }
  .label {
    position: relative;
    width: 892px;
    height: 1200px;
    overflow: hidden;
    background: var(--label-blue);
    font-family: "Archivo Black", "Arial Black", sans-serif;
  }
  .backdrop {
    position: absolute;
    inset: 0;
  }
  .brand-name {
    position: absolute;
    left: 0;
    right: 0;
    top: 100px;
    margin: 0;
    text-align: center;
    color: var(--label-white);
    font-size: 64px;
    font-weight: 400;
    letter-spacing: 1px;
    line-height: 1;
  }
  .product-title {
    position: absolute;
    left: 0;
    right: 0;
    top: 240px;
    margin: 0;
    text-align: center;
    color: var(--label-red);
    font-size: 62px;
    font-weight: 400;
    line-height: 77px;
    -webkit-text-stroke: 8px var(--label-white);
    paint-order: stroke fill;
  }
  .product-photo {
    position: absolute;
    left: 116px;
    top: 502px;
    width: 757px;
    height: 429px;
    border-radius: 180px 120px 60px 110px / 160px 90px 60px 120px;
    background: linear-gradient(180deg, var(--photo-dark) 0%, var(--photo-dark) 28%, var(--photo-light) 42%, #f4f4f4 75%, #c9cbcd 100%);
  }
  .tagline {
    position: absolute;
    left: 51px;
    top: 885px;
    margin: 0;
    color: var(--tag-blue);
    font-size: 35px;
    font-weight: 400;
    line-height: 39px;
  }
  .cleans-list {
    position: absolute;
    left: 51px;
    top: 1033px;
    margin: 0;
    color: var(--label-white);
    font-size: 31px;
    font-weight: 400;
    line-height: 42px;
  }
  .yield {
    position: absolute;
    left: 593px;
    top: 1048px;
    display: flex;
    align-items: flex-end;
    color: var(--ink-black);
    -webkit-text-stroke: 5px var(--label-white);
    paint-order: stroke fill;
  }
  .yield-number {
    font-size: 130px;
    line-height: 110px;
  }
  .yield-words {
    display: flex;
    flex-direction: column;
    font-size: 40px;
    line-height: 46px;
    margin-left: -4px;
    margin-bottom: 4px;
  }
</style>
</head>
<body>
<div class="label">
  <svg class="backdrop" width="892" height="1200" viewBox="0 0 892 1200" aria-hidden="true">
    <path d="M0 640 C 120 600, 220 590, 320 600 L 320 700 C 200 690, 90 700, 0 720 Z" fill="#ffffff"/>
    <path d="M0 684 C 100 650, 200 640, 300 650 L 300 720 C 200 715, 90 735, 0 758 Z" fill="#e8232a"/>
    <path d="M0 877 C 180 800, 420 720, 892 729 L 892 1200 L 0 1200 Z" fill="#ffffff"/>
    <path d="M640 840 C 740 860, 820 890, 892 916 L 892 985 C 820 950, 730 905, 640 880 Z" fill="#4a89c9"/>
    <path d="M0 1020 L 470 1020 C 530 1020, 550 1113, 620 1113 L 892 1113 L 892 1200 L 0 1200 Z" fill="#e8232a"/>
  </svg>

  <h2 class="brand-name">TRACKSIDE</h2>

  <h1 class="product-title">HEAVY DUTY<br>CONVERTIBLE SOFT<br>TOP CLEANER</h1>

  <div class="product-photo" role="img" aria-label="Photo of a white convertible car with a black soft top, seen from the rear three-quarter view"></div>

  <p class="tagline">Quick &amp; Easy<br>To Use For<br>Professional Results</p>

  <p class="cleans-list">cleans: dirt-grime<br>stains - mould<br>and mildew</p>

  <div class="yield">
    <span class="yield-number">2</span>
    <span class="yield-words"><span>Makes</span><span>Liters</span></span>
  </div>
</div>
</body>
</html>
```